Create a Magazine Ad for an asbestos law firm

we need an 8 X 13 ad to be on the back of a magazine cover. We have the text Attached and want a similar look and feel to our website : www.harborvale-claims.example. The ad should be targeted to white males 55 years or older who are conservative and worked in industry or industrial plants. The main offer is a free case review and trying to get them to call the telephone number.

Target Market(s)

White collar men who worked in industrial plants. Age 55 years or older.

Industry/Entity Type

Legal

Requirements
Must have
• Pictures of white middle class conservative man or man and woman
Nice to have
• look at www.harborvale-claims.example to an. idea of what we are looking for

```html
<!DOCTYPE html>
<html lang="en">
<head>
<meta charset="utf-8">
<title>Mesothelioma Compensation – Magazine Ad</title>
<link rel="stylesheet" href="https://fonts.googleapis.com/css2?family=Oswald:wght@500;700&family=Open+Sans:wght@400;600;700&display=swap">
<style>
  :root {
    --ink-deep: #141414;
    --ink-mid: #262626;
    --ink-soft: #333333;
    --gold: #e7b43c;
    --gold-light: #f2c95a;
    --text-light: #f1f1f1;
    --text-muted: #b9b9b9;
    --rule: #4a4a4a;
    --footer-bg: #f3f1ec;
    --footer-ink: #2a2a2a;
  }
  html, body {
    margin: 0;
    padding: 0;
    width: 800px;
    height: 1200px;
    overflow: hidden;
    background: #ffffff;
  }
  .ad {
    position: relative;
    width: 800px;
    height: 1200px;
    overflow: hidden;
    background: radial-gradient(ellipse at 70% 35%, var(--ink-soft) 0%, var(--ink-mid) 40%, var(--ink-deep) 100%);
    font-family: "Open Sans", Arial, sans-serif;
    color: var(--text-light);
  }
  .headline {
    position: absolute;
    top: 34px;
    left: 40px;
    right: 40px;
    margin: 0;
    font-family: "Oswald", "Arial Narrow", sans-serif;
    font-weight: 700;
    font-size: 41px;
    line-height: 1.12;
    letter-spacing: 0.5px;
    text-transform: uppercase;
    text-align: center;
    color: var(--gold);
  }
  .intro {
    position: absolute;
    top: 152px;
    left: 48px;
    width: 380px;
  }
  .lead {
    margin: 0 0 10px;
    font-size: 14px;
    line-height: 1.55;
    font-weight: 600;
  }
  .benefits {
    margin: 0 0 18px;
    padding: 0;
    list-style: none;
    font-size: 12px;
    line-height: 1.7;
    color: var(--text-muted);
  }
  .benefits li::before {
    content: "";
    display: inline-block;
    width: 6px;
    height: 6px;
    margin: 0 8px 1px 0;
    background: var(--gold);
  }
  .qualify {
    margin: 0 0 8px;
    font-size: 15px;
    font-weight: 700;
    line-height: 1.4;
  }
  .section-title {
    margin: 0 0 8px;
    font-family: "Oswald", "Arial Narrow", sans-serif;
    font-weight: 500;
    font-size: 21px;
    line-height: 1.2;
    text-transform: uppercase;
    color: var(--gold);
  }
  .trust {
    position: absolute;
    top: 500px;
    left: 48px;
    width: 380px;
  }
  .trust p {
    margin: 0;
    font-size: 12px;
    line-height: 1.6;
    color: var(--text-muted);
  }
  .payout-question {
    position: absolute;
    top: 660px;
    left: 48px;
    width: 360px;
    margin: 0;
  }
  .portrait {
    position: absolute;
    top: 250px;
    right: 0;
    width: 370px;
    height: 560px;
    background: linear-gradient(180deg, #6a5a4c 0%, #3b332d 35%, #1c1d22 70%, #121316 100%);
  }
  .results {
    position: absolute;
    top: 818px;
    left: 48px;
    right: 48px;
    display: grid;
    grid-template-columns: 1fr 1fr;
    column-gap: 40px;
  }
  .result {
    padding: 12px 0 11px;
    border-top: 1px solid var(--rule);
  }
  .result-amount {
    display: block;
    font-family: "Oswald", "Arial Narrow", sans-serif;
    font-weight: 700;
    font-size: 30px;
    line-height: 1.1;
    color: var(--gold-light);
  }
  .result-label {
    display: block;
    margin-top: 3px;
    font-size: 11px;
    color: var(--text-muted);
    text-transform: uppercase;
    letter-spacing: 0.6px;
  }
  .footer {
    position: absolute;
    left: 0;
    right: 0;
    bottom: 0;
    height: 120px;
    background: var(--footer-bg);
    color: var(--footer-ink);
    text-align: center;
    padding: 22px 60px 0;
    box-sizing: border-box;
  }
  .footer-call {
    margin: 0 0 6px;
    font-size: 13px;
    font-weight: 700;
    text-transform: uppercase;
    line-height: 1.45;
  }
  .footer-call .phone {
    color: #b8861b;
  }
  .footer-note {
    margin: 0;
    font-size: 10px;
    color: #666666;
    text-transform: uppercase;
    letter-spacing: 0.4px;
  }
</style>
</head>
<body>
  <main class="ad">
    <h1 class="headline">Diagnosed with Mesothelioma,<br>You Could Be Owed Compensation</h1>

    <section class="intro">
      <p class="lead">It's very likely you developed this disease through asbestos exposure. Mesothelioma patients are getting multi-million dollar settlements. Benefits may include:</p>
      <ul class="benefits">
        <li>Compensation for medical bills</li>
        <li>Lost wages and income</li>
        <li>Pain and suffering</li>
      </ul>
      <p class="qualify">We can help you find out if you qualify for a case in minutes</p>
      <ul class="benefits">
        <li>Free, no-obligation case review</li>
        <li>No fees unless you win</li>
        <li>Nationwide legal network</li>
      </ul>
    </section>

    <section class="trust">
      <h2 class="section-title">$30 Billion is available in trust<br>for mesothelioma patients</h2>
      <p>Asbestos companies set aside billions in trust funds to compensate workers and veterans who were exposed on the job. You may be entitled to a share, even if the company is no longer in business.</p>
    </section>

    <h2 class="section-title payout-question">How much money can people receive from a mesothelioma case?</h2>

    <div class="portrait" role="img" aria-label="Photo of a bearded man in a dark suit and tie, arms crossed"></div>

    <section class="results">
      <div class="result"><span class="result-amount">$4,142,500</span><span class="result-label">Shipyard worker verdict</span></div>
      <div class="result"><span class="result-amount">$2,150,750</span><span class="result-label">Industrial plant settlement</span></div>
      <div class="result"><span class="result-amount">$5,033,000</span><span class="result-label">Navy veteran settlement</span></div>
      <div class="result"><span class="result-amount">$1,600,400</span><span class="result-label">Power plant worker</span></div>
      <div class="result"><span class="result-amount">$9,820,010</span><span class="result-label">Refinery worker verdict</span></div>
      <div class="result"><span class="result-amount">$2.2 Million</span><span class="result-label">Average trust payout</span></div>
    </section>

    <footer class="footer">
      <p class="footer-call">Call today for your free case review. Speak with a mesothelioma specialist now at <span class="phone">1-800-555-0142</span><br>or visit www.harborvale-claims.example</p>
      <p class="footer-note">Attorney advertising. Prior results do not guarantee a similar outcome.</p>
    </footer>
  </main>
</body>
</html>
```